Valtor Holidays Revamp Project 2015

We are a inbound Travel and tour operator based in Kuala Lumpur, Malaysia, established since 2010. Need a vibrant, dynamic, interactive and user friendly, we expect a Content management system for self data upload.
We cater to different markets around the world form Gulf, to the Far East.
Europe to Africa. With the minimum budget we give maximum services.
The final design should communicate well with the user and portray our growth.

Here is the reference of what our current website looks like.
www.valtorholidays-example.com.my

Target Market(s)

Far-East, South East Asia, Gulf market.

Industry/Entity Type

Travel

Number of Pages Required

5+ page

Font styles to use
Serif
Sans Serif
Other font styles liked:
• Calibri

Requirements
Must have
• User interaction, User friendly, Payment integration, should have a fun interface.
Should not have
• Should not have a complicated and overcrowded or jumbled up layout.

```html
<!DOCTYPE html>
<html lang="en">
<head>
<meta charset="utf-8">
<title>Valtor Holidays</title>
<link href="https://fonts.googleapis.com/css2?family=Raleway:wght@400;500;600;700&family=Open+Sans:wght@400;600;700&family=Teko:wght@500&display=swap" rel="stylesheet">
<style>
:root{
  --red:#c9292f;
  --red-text:#d2262c;
  --ink:#111;
  --grey:#8a8a8a;
  --light:#f7f7f7;
  --tab:#b9b9b9;
  --line:#e6e6e6;
  --footer:#000;
  --white:#fff;
}
*{margin:0;padding:0;box-sizing:border-box}
html,body{width:1200px;height:2970px;overflow:hidden;background:var(--white)}
body{position:relative;font-family:"Open Sans",sans-serif;color:var(--ink)}
.abs{position:absolute}
.brand{display:flex;align-items:center;gap:10px;font-family:"Raleway",sans-serif;font-weight:700;font-size:24px;color:var(--red)}
.brand-dot{width:26px;height:26px;border-radius:50%;background:var(--red)}
.nav{left:0;top:0;width:1200px;height:96px;background:var(--white)}
.nav .brand{position:absolute;left:104px;top:32px}
.menu{position:absolute;left:532px;top:36px;display:flex;list-style:none;font-size:15px;text-transform:uppercase}
.menu li{padding:0 27px;height:34px;line-height:34px;color:#222}
.menu li.active{background:var(--red);color:var(--white);padding:0 18px;margin-right:30px}
.hero{left:0;top:96px;width:1200px;height:464px;background:linear-gradient(180deg,#7fa4a8 0%,#4f7d70 35%,#2d6f86 60%,#1e5a72 100%)}
.hero-title{left:277px;top:386px;width:644px;height:69px;background:var(--red);color:var(--white);font-family:"Teko",sans-serif;font-weight:500;font-size:66px;line-height:78px;text-align:center}
.dots{left:462px;top:514px;display:flex;gap:8px}
.dots span{width:72px;height:4px;background:#dfe8ea}
.dots span.on{background:#111}
.sec-title{left:0;width:1200px;text-align:center;font-family:"Raleway",sans-serif}
.rule{height:3px;background:var(--ink)}
.tabs{left:182px;top:699px;width:792px;height:38px;display:flex}
.tab{flex:1;background:var(--tab);color:#eee;font-size:18px;line-height:38px;text-align:center;position:relative}
.tab.active{background:#000;color:var(--white)}
.tab.active::after{content:"";position:absolute;left:50%;bottom:-8px;margin-left:-8px;border:8px solid transparent;border-bottom:0;border-top-color:#000}
.panel{left:182px;top:737px;width:792px;height:491px;background:var(--light)}
.cost{left:228px;top:775px;font-size:31px;font-weight:700}
.cost-note{left:228px;top:820px;font-size:15px;font-weight:700}
.dash{font-size:16px;color:var(--grey);line-height:32px}
.dash li{list-style:none}
.dash li::before{content:"—";margin-right:14px;color:#bbb}
.incl{left:228px;top:940px;font-size:24px;color:#333}
.divider{left:580px;top:990px;width:1px;height:130px;background:#ddd}
.price-red{left:222px;top:1154px;font-size:14px;color:var(--red)}
.gallery{left:0;top:1307px;width:1200px;height:408px;background:var(--red)}
.photo{position:absolute;top:140px;width:280px;height:180px;border:3px solid var(--white)}
.caption{position:absolute;top:336px;width:280px;text-align:center;color:var(--white);font-size:23px;font-weight:600}
.testi{left:0;top:1715px;width:1200px;height:412px;background:linear-gradient(180deg,#1e2c36 0%,#2a4150 55%,#1d3a45 100%)}
.quote-text{left:152px;top:1862px;width:901px;color:var(--white);font-size:14.5px;line-height:20px;text-align:center}
.quote-mark{left:96px;top:1838px;color:#8a949b;font-size:80px;font-family:Georgia,serif;line-height:1}
.avatar{left:459px;top:1978px;width:76px;height:76px;border-radius:50%;background:linear-gradient(135deg,#b9b0a4,#6f6a64);border:3px solid var(--white)}
.tours-title{top:2188px;font-size:41px;font-weight:500}
.tours-title em{font-style:normal;color:var(--red)}
.tours-sub{top:2246px;font-size:19px;color:#999}
.tour-list{list-style:none;width:350px}
.tour-list li{display:flex;align-items:center;height:41px;border-bottom:1px solid var(--line);font-family:"Raleway",sans-serif;font-size:13px;color:#333}
.tour-list li:last-child{border-bottom:0}
.tour-list svg{margin-right:14px}
.tour-list .price{margin-left:auto;color:#555}
.footer{left:0;top:2641px;width:1200px;height:329px;background:var(--footer);color:var(--white)}
.f-col{position:absolute;top:60px}
.f-col h4{font-family:"Raleway",sans-serif;font-size:14px;font-weight:700;margin-bottom:18px}
.f-text{font-size:12.5px;line-height:23px;color:#ddd}
.f-row{display:flex;gap:12px;font-size:12.5px;line-height:22px;color:#ddd;margin-bottom:8px}
.f-row svg{flex:none;margin-top:5px}
.tags{display:flex;flex-wrap:wrap;gap:6px 6px;width:220px}
.tags span{border:1px solid #777;font-size:9px;padding:6px 10px;letter-spacing:.5px;color:#ccc}
</style>
</head>
<body>

<header class="abs nav">
  <div class="brand"><span class="brand-dot"></span>Valtor Holidays</div>
  <ul class="menu">
    <li class="active">Home</li><li>About Us</li><li>Fencing</li><li>Products</li><li>Contact Us</li>
  </ul>
</header>

<section class="abs hero" role="img" aria-label="Resort with overwater villas, white parasols and a long infinity pool by the sea"></section>
<div class="abs hero-title">travel with us for the best deal</div>
<div class="abs dots"><span class="on"></span><span></span><span></span></div>

<h2 class="abs sec-title" style="top:604px;font-size:35px;font-weight:500">Most Popular Packages</h2>
<div class="abs rule" style="left:560px;top:663px;width:60px"></div>

<div class="abs tabs">
  <div class="tab">3 nights malaysia package</div>
  <div class="tab active">5 nights malaysia package</div>
  <div class="tab">7 nights malaysia package</div>
</div>
<div class="abs panel"></div>
<div class="abs cost">COST:&nbsp; US $299</div>
<div class="abs cost-note">(3 Star Cendana Hotel/ Serai Vista)</div>
<ul class="abs dash" style="left:228px;top:848px">
  <li>3 Nights Cendana Hotel, Kuala lumpur</li>
  <li>2 Night Serai Vista Hotel, Langkawi</li>
</ul>
<div class="abs incl">Package Inclusion :-</div>
<ul class="abs dash" style="left:228px;top:986px;line-height:35px">
  <li>Accommodation with bfast</li>
  <li>Kuala Lumpur Half day City tour</li>
  <li>Kul transfer Klia/Kul/Klia</li>
  <li>All tour &amp; transfer on Pvt basis</li>
</ul>
<div class="abs divider"></div>
<ul class="abs dash" style="left:624px;top:984px;line-height:39px">
  <li>Sunwave Lagoon tour + Ticket</li>
  <li>Langkawi Island Tour</li>
  <li>Lgk transfer Jetty/Htl/Apt</li>
</ul>
<div class="abs price-red">Cost: US$ 299 per person ( 3 Star Cendana Hotel / Serai vista )</div>

<section class="abs gallery">
  <h2 class="sec-title abs" style="top:22px;font-size:34px;font-weight:500;color:var(--white)">Our Gallery</h2>
  <div class="abs" style="left:430px;top:72px;width:304px;height:1px;background:rgba(255,255,255,.6)"></div>
  <div class="abs" style="left:550px;top:71px;width:60px;height:3px;background:var(--white)"></div>
  <div class="photo" style="left:133px;background:linear-gradient(180deg,#2f6fd0,#7aa6d8 55%,#6c8a5a)" role="img" aria-label="City skyline with twin towers under a blue sky"></div>
  <div class="photo" style="left:446px;background:linear-gradient(180deg,#3d8fe0,#7fd3df 50%,#e8e0c8)" role="img" aria-label="Tropical beach with turquoise water and white sand"></div>
  <div class="photo" style="left:758px;background:linear-gradient(180deg,#5a9ad8,#4aa6a0 50%,#2e8a86)" role="img" aria-label="Wooden water villas on stilts over a clear lagoon"></div>
  <div class="caption" style="left:133px">Product 1</div>
  <div class="caption" style="left:446px">Product 2</div>
  <div class="caption" style="left:758px">Product 3</div>
</section>

<section class="abs testi" role="img" aria-label="Dusky tropical bay framed by palm fronds"></section>
<h2 class="abs sec-title" style="top:1754px;font-size:38px;font-weight:500;color:var(--white)">Testimonials</h2>
<div class="abs" style="left:436px;top:1823px;width:312px;height:1px;background:rgba(255,255,255,.5)"></div>
<div class="abs" style="left:560px;top:1822px;width:60px;height:3px;background:var(--white)"></div>
<div class="abs quote-mark">&ldquo;</div>
<p class="abs quote-text">Lorem ipsum dolor sit amet, consectetur adipisicing elit, sed do eiusmod tempor incididunt ut labore et dolore magna aliqua. Ut enim ad minim veniam, quis nostrud exercitation ullamco laboris nisi ut aliquip Ut enim ad minim veniam, quis nostrud.consectetur adipisicing elit, sed do eiusmod tempor We strive to maintain the highest standards while exceed Ut enim ad minim veniam, quis nostrud exercitation ullamco laboris nisi ut aliquip Ut enim ad minim veniam, quis nostrud.consectetur adipisicing&nbsp; aliqua.</p>
<div class="abs avatar" role="img" aria-label="Portrait photo of the reviewer"></div>
<div class="abs" style="left:552px;top:1998px;font-size:13px;color:var(--red-text)">Mara Ellison</div>
<div class="abs" style="left:552px;top:2018px;font-size:13px;font-weight:700;color:var(--white)">chairman</div>

<h2 class="abs sec-title tours-title">Other <em>Popular</em> Tours</h2>
<p class="abs sec-title tours-sub">Quisque at tortor a libero posuere laoreet vitae sed arcu. Curabitur consequat.</p>

<ul class="abs tour-list" style="left:208px;top:2326px">
  <li><svg width="20" height="20" viewBox="0 0 20 20"><circle cx="10" cy="10" r="7" fill="none" stroke="#777" stroke-width="1.5" stroke-dasharray="3 2"/></svg>Tour Eiffel<span class="price">$42</span></li>
  <li><svg width="20" height="20" viewBox="0 0 20 20"><path d="M10 3v14M5 8h10M6 17l4-6 4 6" fill="none" stroke="#777" stroke-width="1.5"/></svg>Shopping tour<span class="price">$35</span></li>
  <li><svg width="20" height="20" viewBox="0 0 20 20"><circle cx="10" cy="10" r="7" fill="none" stroke="#777" stroke-width="1.5" stroke-dasharray="3 2"/></svg>Versailles tour<span class="price">$20</span></li>
  <li><svg width="20" height="20" viewBox="0 0 20 20"><circle cx="10" cy="10" r="7" fill="none" stroke="#777" stroke-width="1.5" stroke-dasharray="3 2"/></svg>Montparnasse skyline<span class="price">$26</span></li>
  <li><svg width="20" height="20" viewBox="0 0 20 20"><rect x="4" y="4" width="12" height="12" fill="none" stroke="#777" stroke-width="1.5"/></svg>Pompidue<span class="price">$26</span></li>
  <li><svg width="20" height="20" viewBox="0 0 20 20"><circle cx="10" cy="10" r="7" fill="none" stroke="#777" stroke-width="1.5" stroke-dasharray="3 2"/></svg>Senna River tour<span class="price">$32</span></li>
</ul>
<ul class="abs tour-list" style="left:600px;top:2326px">
  <li><svg width="20" height="20" viewBox="0 0 20 20"><rect x="4" y="4" width="12" height="12" fill="none" stroke="#777" stroke-width="1.5"/></svg>Notredame<span class="price">$48</span></li>
  <li><svg width="20" height="20" viewBox="0 0 20 20"><path d="M10 3v14M5 8h10M6 17l4-6 4 6" fill="none" stroke="#777" stroke-width="1.5"/></svg>Lafaiette<span class="price">$55</span></li>
  <li><svg width="20" height="20" viewBox="0 0 20 20"><circle cx="10" cy="10" r="7" fill="none" stroke="#777" stroke-width="1.5" stroke-dasharray="3 2"/></svg>Trocadero<span class="price">$76</span></li>
  <li><svg width="20" height="20" viewBox="0 0 20 20"><circle cx="10" cy="10" r="7" fill="none" stroke="#777" stroke-width="1.5" stroke-dasharray="3 2"/></svg>Open Bus tour<span class="price">$55</span></li>
  <li><svg width="20" height="20" viewBox="0 0 20 20"><path d="M10 3v14M5 8h10M6 17l4-6 4 6" fill="none" stroke="#777" stroke-width="1.5"/></svg>Louvre museum<span class="price">$24</span></li>
  <li><svg width="20" height="20" viewBox="0 0 20 20"><circle cx="10" cy="10" r="7" fill="none" stroke="#777" stroke-width="1.5" stroke-dasharray="3 2"/></svg>Madlene Cathedral<span class="price">$24</span></li>
</ul>

<footer class="abs footer">
  <div class="f-col" style="left:125px;top:52px">
    <div class="brand" style="color:var(--white);font-size:21px;margin-bottom:26px"><span class="brand-dot" style="background:var(--white);width:22px;height:22px"></span>Valtor Holidays</div>
    <p class="f-text" style="width:190px">A Powerful &amp; Beautiful Multi-Purpose SitePress theme with tons of advanced features.</p>
    <p style="font-size:11px;color:var(--red-text);margin-top:8px">© Copyright 2015 . All rights reserved</p>
  </div>
  <div class="f-col" style="left:370px">
    <h4>CONTACT INFO</h4>
    <div class="f-row"><svg width="10" height="12" viewBox="0 0 10 12"><path d="M5 0a4 4 0 0 1 4 4c0 3-4 8-4 8S1 7 1 4a4 4 0 0 1 4-4z" fill="#fff"/></svg><span>418/12 Harbour Lane,<br>Eastwick, Mill Street,<br>Northfield United Kingdom</span></div>
    <div class="f-row"><svg width="10" height="12" viewBox="0 0 10 12"><path d="M2 0h2l1 3-1.5 1a6 6 0 0 0 3 3L8 5.5l2 1v2.5C5 9 1 5 1 1z" fill="#fff"/></svg>345-600-118</div>
    <div class="f-row"><svg width="10" height="12" viewBox="0 0 10 12"><rect x="2" y="0" width="6" height="12" rx="1" fill="none" stroke="#fff" stroke-width="1.4"/></svg>323-600-142</div>
    <div class="f-row"><svg width="12" height="10" viewBox="0 0 12 10"><rect width="12" height="9" fill="#fff"/><path d="M0 0l6 5 6-5" fill="none" stroke="#000"/></svg>info@valtorholidays.example</div>
    <div class="f-row"><svg width="12" height="12" viewBox="0 0 12 12"><circle cx="6" cy="6" r="5.5" fill="#fff"/></svg>valtorholidays.example</div>
  </div>
  <div class="f-col" style="left:610px">
    <h4>RECENT POSTS</h4>
    <p class="f-text" style="line-height:33px;margin-top:-6px">Standard Blog Post With Image<br>Amazing Fullwidth Post<br>Link Post<br>Quote Post<br>Sidebar Post With Slideshow</p>
  </div>
  <div class="f-col" style="left:850px">
    <h4>TAGS</h4>
    <div class="tags"><span>BLOG</span><span>CITY</span><span>DESIGN</span><span>LANDSCAPE</span><span>MODEL</span><span>PORTRAIT</span><span>STREET</span><span>STREET PHOTOGRAPHY</span></div>
  </div>
</footer>

</body>
</html>
```